Stationery Design Project

We need a stationery design for a new business consulting business based in New Zealand.
We have the logo and business cards designed and we're looking for letterhead, compliments slip and PowerPoint presentation format that aligns with our business cards.
Industry/Entity Type
Business
Requirements
Must have
- same colors and format as business cards

```html
<!DOCTYPE html>
<html lang="en">
<head>
<meta charset="utf-8">
<title>Kauri Advisory – Stationery Suite</title>
<link href="https://fonts.googleapis.com/css2?family=Questrial&family=Open+Sans:wght@400;700&display=swap" rel="stylesheet">
<style>
  :root{
    --green:#8cc63f;
    --grey:#8c8c8c;
    --grey-dark:#6b6b6b;
    --grey-bar:#9a9a9a;
    --page-bg:#e2e2e2;
    --panel-bg:#ececec;
    --paper:#ffffff;
    --taupe:#b3aaa2;
    --taupe-light:#ddd8d3;
    --line-pink:#e3a3a3;
    --text-soft:#a8a8a8;
  }
  *{margin:0;padding:0;box-sizing:border-box}
  html,body{width:1200px;height:2618px;overflow:hidden}
  body{background:var(--page-bg);position:relative;font-family:"Questrial",sans-serif;color:var(--grey-dark)}
  .abs{position:absolute}
  .brand-name{font-family:"Questrial",sans-serif;color:var(--green);white-space:nowrap;line-height:1}

  .stationery-panel{left:22px;top:0;width:1156px;height:1527px;background:var(--panel-bg)}

  /* Folder */
  .folder{left:65px;top:92px;width:491px;height:693px;background:radial-gradient(circle at 50% 35%,#fff 0%,#eee 45%,#d9d9d9 100%)}
  .folder .band-green-top{left:0;top:0;width:100%;height:13px;background:var(--green)}
  .folder .band-grey-top{left:0;top:13px;width:100%;height:30px;background:var(--grey-bar)}
  .folder .brand-name{left:0;width:100%;top:170px;text-align:center;font-size:44px}
  .folder .band-green-bottom{left:0;bottom:11px;width:100%;height:29px;background:var(--green);color:#fff;font-family:"Open Sans",sans-serif;font-weight:700;font-size:13px;text-align:center;line-height:29px}
  .folder .band-grey-bottom{left:0;bottom:0;width:100%;height:11px;background:var(--grey-bar)}

  /* Letterhead */
  .letterhead{left:583px;top:92px;width:493px;height:689px;background:var(--paper)}
  .letterhead .band-green{right:0;top:0;width:181px;height:19px;background:var(--green)}
  .letterhead .brand-name{left:34px;top:44px;font-size:28px}
  .letterhead .contact{left:312px;top:26px;font-size:8px;line-height:10px;color:var(--grey)}
  .letterhead .contact .person{color:var(--green);font-size:11px;font-family:"Open Sans",sans-serif;font-weight:700;line-height:13px}
  .letterhead .side-bar{left:0;top:170px;width:19px;height:454px;background:var(--grey-bar)}
  .letter-body{left:46px;top:170px;width:400px;font-family:"Open Sans",sans-serif;font-size:8px;line-height:11px;color:var(--text-soft)}
  .letter-body .date{text-align:right;margin-bottom:20px}
  .letter-body p{margin-bottom:11px}

  /* Business card */
  .business-card{left:227px;top:823px;width:694px;height:327px;background:radial-gradient(circle at 40% 40%,#f6f6f6 0%,#e4e4e4 60%,#d4d4d4 100%)}
  .business-card .band-green{right:0;top:0;width:349px;height:28px;background:var(--green)}
  .business-card .brand-name{left:145px;top:90px;font-size:42px}
  .business-card .side-bar{left:0;top:185px;width:30px;height:142px;background:var(--grey-bar)}
  .business-card .contact{left:59px;top:190px;font-size:12px;line-height:15px;color:var(--grey)}
  .business-card .contact .person{color:var(--green);font-family:"Open Sans",sans-serif;font-weight:700;font-size:16px;line-height:18px}
  .business-card .contact .role{font-size:10px;margin-bottom:10px}
  .contact-line{display:flex;align-items:center;gap:5px}
  .contact-line svg{width:11px;height:11px;flex:none}

  /* Compliments slip */
  .compliments-slip{left:227px;top:1174px;width:694px;height:327px;background:radial-gradient(circle at 18% 50%,#f7f7f7 0%,#e2e2e2 55%,#d3d3d3 100%)}
  .compliments-slip .brand-name{left:36px;top:148px;font-size:36px}
  .compliments-slip .slip-text{left:351px;top:90px;width:295px;font-family:"Open Sans",sans-serif;font-size:9px;line-height:12px;color:var(--text-soft)}
  .compliments-slip .slip-heading{color:var(--green);font-weight:700;font-size:11px;text-decoration:underline;margin-bottom:6px}

  /* Presentation slides */
  .slide{left:430px;width:438px;background:linear-gradient(180deg,#f7f4f0 0%,#ece6e0 100%);box-shadow:0 2px 6px rgba(0,0,0,.25)}
  .slide .band-bottom{left:0;bottom:0;width:100%;height:18px;background:var(--taupe)}
  .slide-title{top:1534px;height:321px;background:#fff}
  .slide-title .band-green{left:0;top:0;width:100%;height:28px;background:var(--green)}
  .slide-title .logo-box{left:46px;top:66px;width:347px;height:157px;background:var(--taupe-light);border-radius:20px;display:flex;align-items:center;justify-content:center}
  .slide-title .logo-box .brand-name{position:static;font-size:38px}
  .slide-title .enter-text{left:0;width:100%;top:254px;text-align:center;font-family:"Open Sans",sans-serif;font-weight:700;font-size:20px;color:var(--grey-dark)}
  .slide-content{height:332px}
  .slide-content .band-green{right:0;top:4px;width:28px;height:76px;background:var(--green)}
  .slide-content .brand-name{left:67px;top:36px;font-size:26px}
  .slide-bullets{top:1894px}
  .slide-columns{top:2258px}
  .slide-heading{font-family:"Open Sans",sans-serif;font-weight:700;font-size:10px;color:var(--green)}
  .bullet-list{list-style:none}
  .bullet-list li{height:5px;background:var(--line-pink);border-radius:2px;margin-bottom:6px;position:relative}
  .bullet-list li::before{content:"";position:absolute;left:-9px;top:1px;width:3px;height:3px;border-radius:50%;background:var(--green)}
</style>
</head>
<body>

<div class="abs stationery-panel"></div>

<section class="abs folder" aria-label="Presentation folder">
  <div class="abs band-green-top"></div>
  <div class="abs band-grey-top"></div>
  <div class="abs brand-name">Kauri Advisory</div>
  <div class="abs band-green-bottom">www.kauriadvisory.co.nz</div>
  <div class="abs band-grey-bottom"></div>
</section>

<section class="abs letterhead" aria-label="Letterhead">
  <div class="abs band-green"></div>
  <div class="abs brand-name">Kauri Advisory</div>
  <div class="abs contact">
    <div class="person">CONSULTANT NAME</div>
    <div>Senior Advisor</div>
    <div>PO Box 40718</div>
    <div>Nelson 7010 New Zealand</div>
    <div>+64 21 555 0148</div>
    <div>hello@kauriadvisory.co.nz</div>
    <div>www.kauriadvisory.co.nz</div>
  </div>
  <div class="abs side-bar"></div>
  <div class="abs letter-body">
    <div class="date">14 March 2025</div>
    <div>Client Name</div>
    <div style="margin-bottom:11px">Company Ltd</div>
    <p>Dear Client,</p>
    <p>Thank you for meeting with our team last week to discuss the next stage of your business plan. We have reviewed the figures you shared and prepared a short outline of the options we believe will deliver the strongest results for your company over the coming year.</p>
    <p>Our proposal covers strategy, finance and staff planning, with clear steps and simple reporting at each stage. We will work alongside your managers to set goals, track progress and adjust the plan as the market changes.</p>
    <p>Please let us know a suitable time to talk through the details. We look forward to working with you.</p>
    <p style="margin-bottom:22px">Kind regards,</p>
    <div>Consultant Name</div>
  </div>
</section>

<section class="abs business-card" aria-label="Business card">
  <div class="abs band-green"></div>
  <div class="abs brand-name">Kauri Advisory</div>
  <div class="abs side-bar"></div>
  <div class="abs contact">
    <div class="person">CONSULTANT NAME</div>
    <div class="role">Senior Advisor</div>
    <div>PO Box 40718</div>
    <div>Nelson 7010 New Zealand</div>
    <div class="contact-line"><svg viewBox="0 0 12 12"><path d="M3 1l2 2-1 2c1 1.5 2 2.5 3 3l2-1 2 2-1.5 2C5 11 1 7 1 2.5z" fill="none" stroke="var(--green)" stroke-width="1.2"/></svg>+64 21 555 0148</div>
    <div class="contact-line"><svg viewBox="0 0 12 12"><rect x="1" y="2.5" width="10" height="7" fill="none" stroke="var(--green)" stroke-width="1.2"/><path d="M1 2.5l5 4 5-4" fill="none" stroke="var(--green)" stroke-width="1.2"/></svg>hello@kauriadvisory.co.nz</div>
    <div class="contact-line"><svg viewBox="0 0 12 12"><circle cx="6" cy="6" r="4.8" fill="none" stroke="var(--green)" stroke-width="1.2"/><path d="M1.2 6h9.6M6 1.2c-2 2.5-2 7.1 0 9.6M6 1.2c2 2.5 2 7.1 0 9.6" fill="none" stroke="var(--green)" stroke-width="1"/></svg>www.kauriadvisory.co.nz</div>
  </div>
</section>

<section class="abs compliments-slip" aria-label="Compliments slip">
  <div class="abs brand-name">Kauri Advisory</div>
  <div class="abs slip-text">
    <div class="slip-heading">KAURI ADVISORY</div>
    <p>With compliments from our team. We hope this information is helpful and look forward to speaking with you soon about your plans. Please contact us at any time for further advice.</p>
  </div>
</section>

<section class="abs slide slide-title" aria-label="Title slide">
  <div class="abs band-green"></div>
  <div class="abs logo-box"><span class="brand-name">Kauri Advisory</span></div>
  <div class="abs enter-text">ENTER TEXT HERE</div>
  <div class="abs band-bottom"></div>
</section>

<section class="abs slide slide-content slide-bullets" aria-label="Bullet slide">
  <div class="abs band-green"></div>
  <div class="abs brand-name">Kauri Advisory</div>
  <div class="abs" style="left:72px;top:122px;width:240px">
    <div class="slide-heading" style="margin-bottom:6px">– Enter Title Here</div>
    <ul class="bullet-list" style="margin-left:16px">
      <li style="width:200px"></li><li style="width:210px"></li><li style="width:228px"></li><li style="width:186px"></li>
    </ul>
  </div>
  <div class="abs" style="left:72px;top:218px;width:240px">
    <div class="slide-heading" style="margin-bottom:6px">– Enter Title Here</div>
    <ul class="bullet-list" style="margin-left:16px">
      <li style="width:212px"></li><li style="width:200px"></li><li style="width:205px"></li><li style="width:180px"></li>
    </ul>
  </div>
  <div class="abs band-bottom"></div>
</section>

<section class="abs slide slide-content slide-columns" aria-label="Two column slide">
  <div class="abs band-green"></div>
  <div class="abs brand-name">Kauri Advisory</div>
  <div class="abs" style="left:28px;top:106px;width:170px">
    <div class="slide-heading" style="margin-bottom:14px">TITLE 2</div>
    <ul class="bullet-list" style="margin-left:12px">
      <li style="width:150px"></li><li style="width:150px"></li><li style="width:150px"></li><li style="width:150px"></li><li style="width:150px"></li><li style="width:150px"></li><li style="width:150px"></li>
    </ul>
  </div>
  <div class="abs" style="left:233px;top:106px;width:170px">
    <div class="slide-heading" style="margin-bottom:14px">TITLE 2</div>
    <ul class="bullet-list" style="margin-left:12px">
      <li style="width:150px"></li><li style="width:150px"></li><li style="width:150px"></li><li style="width:150px"></li><li style="width:150px"></li><li style="width:150px"></li><li style="width:150px"></li>
    </ul>
  </div>
  <div class="abs band-bottom"></div>
</section>

</body>
</html>
```